Orvella Aid Fund - New Website Design

I need a site that looks like this http://renwick-gives-now.org for boat donations. So please replace the cars with boats.

```html
<!DOCTYPE html>
<html lang="en">
<head>
<meta charset="utf-8">
<title>Orvella Aid Fund – Boat Donations</title>
<link rel="stylesheet" href="https://fonts.googleapis.com/css2?family=Poppins:wght@300;400;500;600;700&display=swap">
<style>
:root{
  --red:#e8262d;
  --purple:#8b3f9d;
  --purple-dark:#6f2f80;
  --ink:#222222;
  --body:#444444;
  --muted:#777777;
  --grey-band:#ebebeb;
  --footer:#d9d9d9;
  --faq-item:#c9c9c9;
  --white:#ffffff;
  --line:#cfcfcf;
  --link-blue:#1d4f9e;
}
*{box-sizing:border-box;margin:0;padding:0}
html,body{width:1200px;height:2616px;overflow:hidden}
body{position:relative;font-family:'Poppins',sans-serif;color:var(--ink);background:var(--white)}
.abs{position:absolute}

/* header */
.site-header{left:0;top:0;width:1200px;height:101px;background:#efeeec}
.brand{display:flex;align-items:center;gap:10px}
.brand-dot{width:34px;height:34px;border-radius:50%;background:var(--purple)}
.brand-name{font-weight:700;font-size:19px;color:var(--purple);letter-spacing:.3px;text-transform:uppercase}
.header-brand{left:173px;top:30px}
.phone{left:672px;top:36px;display:flex;align-items:center;gap:9px;font-weight:600;font-size:18px;color:var(--ink)}
.donate-btn{left:835px;top:29px;width:160px;height:40px;background:var(--purple);color:var(--white);font-weight:600;font-size:16px;display:flex;align-items:center;padding-left:20px;border-radius:3px}
.donate-badge{left:960px;top:13px;width:68px;height:68px;border-radius:50%;background:var(--purple);display:flex;align-items:center;justify-content:center}

/* nav */
.main-nav{left:0;top:101px;width:1200px;height:42px;background:var(--red)}
.main-nav ul{list-style:none;display:flex;position:absolute;left:173px;top:0;height:42px}
.main-nav li{font-size:13px;color:var(--white);text-transform:uppercase;padding:0 22px;line-height:42px}
.main-nav li.active{background:#262626}

/* hero */
.hero{left:0;top:143px;width:1200px;height:410px;background:linear-gradient(100deg,#5a6470 0%,#8a7a70 30%,#b6aca2 60%,#d8d2cb 100%)}
.hero-title{right:558px;top:200px;text-align:right;color:var(--white);font-weight:700;font-size:44px;line-height:46px;text-shadow:0 2px 4px rgba(0,0,0,.25)}
.hero-tag{left:324px;top:302px;background:var(--red);color:var(--white);font-size:19px;padding:2px 10px;line-height:30px}

/* form */
.pickup-form{left:670px;top:87px;width:356px;height:384px;background:var(--white);box-shadow:0 3px 10px rgba(0,0,0,.25)}
.form-title{left:0;top:12px;width:356px;text-align:center;font-size:26px;font-weight:400}
.form-rule{left:0;top:56px;width:356px;height:1px;background:var(--line)}
.form-label{left:15px;font-size:13px;font-weight:600;color:var(--red)}
.field{height:33px;border:1px solid #cfcfcf;font-size:11px;color:#555;padding-left:9px;line-height:31px;background:var(--white)}
.field.select::after{content:"›";position:absolute;right:9px;top:0;font-size:14px}
.submit-btn{left:90px;top:328px;width:177px;height:35px;background:var(--purple);color:var(--white);font-weight:600;font-size:13px;text-align:center;line-height:35px;text-transform:uppercase;border-radius:2px}

/* welcome */
.welcome{left:0;top:553px;width:1200px;height:319px;background:var(--grey-band)}
.section-title{width:1200px;left:0;text-align:center;font-size:38px;font-weight:400;color:var(--ink)}
.section-title em{font-style:normal;color:var(--red)}
.welcome-copy{left:195px;top:130px;width:810px;text-align:center;font-size:11.5px;line-height:23px;color:var(--body)}
.welcome-copy p+p{margin-top:22px}

/* features */
.features{left:0;top:872px;width:1200px;height:579px;background:var(--white)}
.subtitle{left:0;top:91px;width:1200px;text-align:center;font-size:14px;color:var(--body)}
.title-rule{height:2px;width:80px;background:var(--ink);left:560px}
.feature-label{font-size:12.5px;font-weight:500;line-height:22px;color:#333;letter-spacing:.3px}
.feature-label.left{text-align:right}

/* faq */
.faq-band{left:0;top:1451px;width:1200px;height:537px;background:linear-gradient(90deg,#8fb6cf 0%,#c9d9e2 35%,#eef1f2 65%,#f7f7f7 100%)}
.faq-box{left:539px;top:1500px;width:487px;height:432px;background:rgba(255,255,255,.92)}
.faq-title{left:24px;top:18px;font-size:28px;font-weight:400}
.faq-title em{font-style:normal;color:var(--red)}
.faq-item{left:28px;width:432px;height:32px;font-size:12px;line-height:32px;padding:0 16px;color:#555;background:var(--faq-item);border:1px solid #b8b8b8}
.faq-item span{position:absolute;right:14px;top:0}
.faq-item.open{background:var(--red);color:var(--white);border-color:var(--red)}
.faq-answer{left:44px;top:125px;width:405px;font-size:11px;line-height:19px;color:#444}

/* stories */
.stories{left:0;top:1988px;width:1200px;height:314px;background:var(--white)}
.story-text{left:220px;top:154px;width:760px;text-align:center;font-size:15px;line-height:26px;color:var(--body)}
.story-name{left:0;top:221px;width:1200px;text-align:center;font-size:13px;font-weight:600;color:var(--link-blue)}
.story-date{left:0;top:245px;width:1200px;text-align:center;font-size:10px;color:var(--muted)}
.arrow{top:178px;font-size:30px;color:#999;font-weight:300}

/* footer */
.site-footer{left:0;top:2302px;width:1200px;height:314px;background:var(--footer)}
.footer-nav{left:0;top:62px;width:1200px;display:flex;justify-content:center;gap:30px;font-size:13px;text-transform:uppercase;color:#333}
.copyright{left:0;top:94px;width:1200px;text-align:center;font-size:11px;color:#555}
.social{left:0;top:140px;width:1200px;display:flex;justify-content:center;gap:32px}
.social span{width:30px;height:30px;border-radius:50%;background:#444}
.footer-brand{left:0;top:210px;width:1200px;justify-content:center}
</style>
</head>
<body>

<header class="site-header abs">
  <div class="brand header-brand abs"><span class="brand-dot"></span><span class="brand-name">Orvella Aid Fund</span></div>
  <div class="phone abs">
    <svg width="16" height="16" viewBox="0 0 16 16"><rect width="16" height="16" rx="3" fill="#e8262d"/><path d="M5 3.5l2 2-1 1.3c.6 1.3 1.6 2.3 2.9 2.9l1.3-1 2 2-1.3 1.6C7.5 12.2 3.8 8.5 3.5 4.8z" fill="#fff"/></svg>
    555-014-2290
  </div>
  <div class="donate-btn abs">Donate Now</div>
  <div class="donate-badge abs">
    <svg width="38" height="36" viewBox="0 0 38 36" fill="none" stroke="#fff" stroke-width="2"><path d="M19 22s-9-5.5-9-11a4.5 4.5 0 0 1 9-1 4.5 4.5 0 0 1 9 1c0 5.5-9 11-9 11z"/><path d="M3 20l6 10h8M35 20l-6 10h-8"/></svg>
  </div>
</header>

<nav class="main-nav abs">
  <ul><li class="active">Home</li><li>About Us</li><li>Get Started</li><li>Contact Us</li></ul>
</nav>

<section class="hero abs" role="img" aria-label="Photo of a smiling young child wearing a knit cap, resting on folded arms"></section>
<h1 class="hero-title abs">Donate Boat to<br>Charity!</h1>
<div class="hero-tag abs">Your Boat can make a different!</div>

<form class="pickup-form abs">
  <h2 class="form-title abs">Donation Pick Up Form</h2>
  <div class="form-rule abs"></div>
  <div class="form-label abs" style="top:66px">Contact Information</div>
  <div class="field abs" style="left:15px;top:91px;width:159px">First Name</div>
  <div class="field abs" style="left:183px;top:91px;width:158px">Last Name</div>
  <div class="field abs" style="left:15px;top:131px;width:159px">Zip Code</div>
  <div class="field abs" style="left:183px;top:131px;width:158px">Day Phone</div>
  <div class="field abs" style="left:15px;top:171px;width:326px">Email Address</div>
  <div class="form-label abs" style="top:220px">Boat Donation Information</div>
  <div class="field select abs" style="left:15px;top:243px;width:159px">Choose Year</div>
  <div class="field select abs" style="left:183px;top:243px;width:158px">Choose Make</div>
  <div class="field abs" style="left:15px;top:285px;width:326px">Model of Boat</div>
  <div class="submit-btn abs">Submit Application</div>
</form>

<section class="welcome abs">
  <h2 class="section-title abs" style="top:38px">Welcome to <em>Orvella Aid Fund</em></h2>
  <div class="welcome-copy abs">
    <p>Lorem Ipsum is simply dummy text of the printing and typesetting industry. Lorem Ipsum has been the industry's standard dummy text ever since the 1500s, when an unknown printer took a galley of type and scrambled it to make a type specimen book. It has survived not only five centuries, but also the leap into electronic typesetting, remaining essentially unchanged.</p>
    <p>Lorem Ipsum is simply dummy text of the printing and typesetting industry. Lorem Ipsum has been the industry's standard dummy text ever since the 1500s, when an unknown printer took a galley of type and scrambled.</p>
  </div>
</section>

<section class="features abs">
  <h2 class="section-title abs" style="top:38px">Donate Boats To <em>Charity!</em></h2>
  <p class="subtitle abs">Your boat can make a difference!</p>
  <div class="title-rule abs" style="top:121px"></div>

  <svg class="abs" style="left:0;top:0" width="1200" height="579" viewBox="0 0 1200 579">
    <g stroke="#4f6fb0" stroke-width="1.5" fill="#c9d3ea">
      <line x1="466" y1="226" x2="514" y2="263"/><line x1="426" y1="344" x2="480" y2="344"/><line x1="466" y1="462" x2="514" y2="425"/>
      <line x1="732" y1="226" x2="684" y2="263"/><line x1="772" y1="344" x2="718" y2="344"/><line x1="732" y1="462" x2="684" y2="425"/>
      <circle cx="514" cy="263" r="5"/><circle cx="480" cy="344" r="5"/><circle cx="514" cy="425" r="5"/>
      <circle cx="684" cy="263" r="5"/><circle cx="718" cy="344" r="5"/><circle cx="684" cy="425" r="5"/>
    </g>
    <circle cx="599" cy="344" r="119" fill="#fff" stroke="#9a9a9a" stroke-width="2" stroke-dasharray="2 3"/>
    <g fill="#fff" stroke="#d9d9d9" stroke-width="4">
      <circle cx="433" cy="204" r="38"/><circle cx="389" cy="344" r="38"/><circle cx="433" cy="483" r="38"/>
      <circle cx="765" cy="204" r="38"/><circle cx="809" cy="344" r="38"/><circle cx="765" cy="483" r="38"/>
    </g>
    <g fill="#8b3f9d">
      <circle cx="433" cy="204" r="32"/><circle cx="389" cy="344" r="32"/><circle cx="433" cy="483" r="32"/>
      <circle cx="765" cy="204" r="32"/><circle cx="809" cy="344" r="32"/><circle cx="765" cy="483" r="32"/>
    </g>
    <g fill="none" stroke="#fff" stroke-width="2" stroke-linejoin="round" stroke-linecap="round">
      <path d="M417 208h32l-5 9h-22z M425 208v-12h12v12"/>
      <path d="M371 347h36l-6 9h-24z M380 347v-10h16l4 10"/>
      <path d="M423 490l14-14 M430 474l8 8 M418 497h16 M446 490a8 8 0 1 0 1 0"/>
      <path d="M765 219s-15-9-15-18a7 7 0 0 1 15-2 7 7 0 0 1 15 2c0 9-15 18-15 18z"/>
      <path d="M793 354h10l8 4h10M800 336h16v10h-16z"/>
      <path d="M774 472c-3-3-14-3-14 3s14 3 14 9-11 6-15 2M767 466v36"/>
    </g>
  </svg>
  <div class="abs" role="img" aria-label="Illustration of four cartoon children standing on letter blocks" style="left:520px;top:270px;width:158px;height:150px;border-radius:50%;background:radial-gradient(circle,#f3c67a 0%,#9ccf8e 45%,#fff 72%)"></div>

  <div class="feature-label left abs" style="right:823px;top:183px">Free Towing In<br>48-24 Hours</div>
  <div class="feature-label left abs" style="right:868px;top:322px">We Accept<br>All Boats</div>
  <div class="feature-label left abs" style="right:823px;top:461px">Boat Will Be Sold on the<br>Largest Auction Network</div>
  <div class="feature-label abs" style="left:823px;top:183px">Boat Donations Help Fund<br>Charitable Programs</div>
  <div class="feature-label abs" style="left:866px;top:322px">Hassle<br>Free Donation</div>
  <div class="feature-label abs" style="left:823px;top:461px">Income<br>Tax Deduction</div>
</section>

<section class="faq-band abs" role="img" aria-label="Photo of a child in a blue headscarf hugging a plush toy by a window"></section>
<div class="faq-box abs">
  <h2 class="faq-title abs">Frequently Asked <em>Questions</em></h2>
  <div class="faq-item open abs" style="top:70px">What types of boats can be donated?<span>−</span></div>
  <p class="faq-answer abs">We accept all boat donations, and in most cases, we also accept cars, motorcycles, RV's, and campers.</p>
  <div class="faq-item abs" style="top:192px">What paperwork do I need to donate my boat?<span>+</span></div>
  <div class="faq-item abs" style="top:226px">Is my donated boat tax-deductible?<span>+</span></div>
  <div class="faq-item abs" style="top:260px">What if the boat is not registered in my name?<span>+</span></div>
  <div class="faq-item abs" style="top:294px">How much will I receive as a tax deduction for my boat?<span>+</span></div>
  <div class="faq-item abs" style="top:328px">When will I receive my tax receipt?<span>+</span></div>
  <div class="faq-item abs" style="top:362px">How do I schedule a pick up?<span>+</span></div>
</div>

<section class="stories abs">
  <h2 class="section-title abs" style="top:46px">Success <em>Stories</em></h2>
  <div class="title-rule abs" style="top:104px"></div>
  <p class="story-text abs">Lorem Ipsum is simply dummy text of the printing and typesetting industry. Lorem Ipsum has been the industry's standard dummy text ever since the 1500s</p>
  <div class="story-name abs">by Dessa R.</div>
  <div class="story-date abs">March 2012</div>
  <div class="arrow abs" style="left:166px">‹</div>
  <div class="arrow abs" style="left:1018px">›</div>
</section>

<footer class="site-footer abs">
  <div class="footer-nav abs"><span>Home</span><span>/</span><span>About Us</span><span>/</span><span>Get Started</span><span>/</span><span>Contact Us</span></div>
  <div class="copyright abs">Copyright © 2017 Orvella Aid Fund. All rights reserved.</div>
  <div class="social abs"><span></span><span></span><span></span><span></span><span></span><span></span></div>
  <div class="brand footer-brand abs"><span class="brand-dot"></span><span class="brand-name">Orvella Aid Fund</span></div>
</footer>

</body>
</html>
```